Require stock illustrations for BrimQuay website

We need the 8 screenshots in the 'Features' section (also attached) to be individually recreated as illustrations using a style/colors similar to the image on the home page:

http://images.brimquay-example.com/AgentPictures/BrimQuayV2/template/index.html#_

The illustrations are meant to be abstract versions of the actual images

Font styles to use
Sans Serif

Requirements
Must have
• 1. 8 vector images including png outputs
2. style of images should match the style/colors of the image on the home page
3. all images should possess the same aspect ratio of 545 width x 344 height

```html
<!DOCTYPE html>
<html lang="en">
<head>
<meta charset="utf-8">
<title>BrimQuay Dashboard Illustration</title>
<link rel="stylesheet" href="https://fonts.googleapis.com/css2?family=Open+Sans:wght@400;600;700&display=swap">
<style>
  :root{
    --page:#f4f4f4;
    --card:#ffffff;
    --line:#e3e3e3;
    --ph-dark:#a9a9a9;
    --ph:#c6c6c6;
    --ph-light:#d6d6d6;
    --teal:#2bbfc7;
    --orange:#ff6633;
    --yellow:#ffd35c;
    --slate:#686e78;
    --green:#8cc63f;
    --green-band:#def0d6;
    --blue-band:#d8edf6;
    --ink:#555a60;
  }
  *{box-sizing:border-box;margin:0;padding:0}
  html,body{width:1200px;height:757px;overflow:hidden;background:var(--page);font-family:"Open Sans",Arial,sans-serif}
  .canvas{position:relative;width:1200px;height:757px}
  .abs{position:absolute}
  .bar{position:absolute;border-radius:2px;background:var(--ph)}
  .topnav{left:0;top:0;width:1200px;height:40px;background:var(--card)}
  .header-box{left:9px;top:44px;width:1180px;height:57px;background:var(--card)}
  .band{left:9px;width:1180px;height:33px}
  .band--success{top:112px;background:var(--green-band)}
  .band--info{top:158px;background:var(--blue-band)}
  .pill{position:absolute;height:9px;border-radius:5px}
  .band-plus{position:absolute;right:12px;top:8px;font-size:13px;color:#9aa;line-height:1}
  .stat{top:207px;width:279px;height:77px;background:var(--card);display:flex}
  .stat__icon{width:113px;height:77px;display:flex;align-items:center;justify-content:center}
  .stat__body{flex:1;position:relative}
  .stat__value{position:absolute;left:0;right:0;top:18px;text-align:center;font-size:23px;font-weight:600;color:var(--ink);letter-spacing:.5px}
  .stat__label{position:absolute;left:50%;top:50px;width:22px;height:5px;margin-left:-11px;border-radius:2px;background:var(--ph)}
  .chart-panel{left:20px;top:326px;width:1158px;height:391px;background:var(--card)}
</style>
</head>
<body>
<div class="canvas">

  <nav class="abs topnav">
    <span class="bar" style="left:18px;top:16px;width:56px;height:5px"></span>
    <span class="bar" style="left:84px;top:16px;width:44px;height:5px"></span>
    <span class="bar" style="left:141px;top:16px;width:46px;height:5px"></span>
    <span class="bar" style="left:1134px;top:16px;width:52px;height:5px"></span>
  </nav>

  <header class="abs header-box">
    <span class="bar" style="left:9px;top:15px;width:108px;height:8px;background:var(--ph-dark)"></span>
    <span class="bar" style="left:9px;top:33px;width:184px;height:6px;background:var(--ph-light)"></span>
    <svg class="abs" style="right:18px;top:22px" width="12" height="12" viewBox="0 0 12 12" aria-hidden="true">
      <circle cx="5" cy="5" r="3.5" fill="none" stroke="#aaa" stroke-width="1.5"/><path d="M7.5 7.5l3 3" stroke="#aaa" stroke-width="1.5"/>
    </svg>
  </header>

  <div class="abs band band--success">
    <span class="bar" style="left:9px;top:13px;width:308px;height:6px"></span>
    <span class="pill" style="left:317px;top:12px;width:26px;background:var(--orange)"></span>
    <span class="band-plus">+</span>
  </div>

  <div class="abs band band--info">
    <span class="bar" style="left:9px;top:14px;width:163px;height:6px"></span>
    <span class="pill" style="left:176px;top:12px;width:29px;background:var(--teal)"></span>
    <span class="bar" style="left:209px;top:14px;width:62px;height:6px"></span>
    <span class="pill" style="left:273px;top:12px;width:29px;background:var(--green)"></span>
    <span class="band-plus">+</span>
  </div>

  <section class="abs stat" style="left:9px">
    <div class="stat__icon" style="background:var(--teal)">
      <svg width="44" height="30" viewBox="0 0 44 30" aria-hidden="true">
        <path d="M3 15C9 6 16 3 22 3s13 3 19 12c-6 9-13 12-19 12S9 24 3 15z" fill="none" stroke="#fff" stroke-width="3"/>
        <circle cx="22" cy="15" r="6" fill="none" stroke="#fff" stroke-width="3"/>
      </svg>
    </div>
    <div class="stat__body"><div class="stat__value">14087</div><span class="stat__label"></span></div>
  </section>

  <section class="abs stat" style="left:310px">
    <div class="stat__icon" style="background:var(--orange)">
      <svg width="34" height="34" viewBox="0 0 34 34" aria-hidden="true">
        <rect x="2" y="2" width="30" height="30" rx="5" fill="none" stroke="#fff" stroke-width="3"/>
        <path d="M11 8c2 0 3 4 2 5l-1 1c1 3 4 6 7 7l1-1c1-1 5 0 5 2l-1 3c-8 1-16-7-15-15z" fill="#fff"/>
      </svg>
    </div>
    <div class="stat__body"><div class="stat__value">596</div><span class="stat__label"></span></div>
  </section>

  <section class="abs stat" style="left:610px">
    <div class="stat__icon" style="background:var(--yellow)">
      <svg width="34" height="34" viewBox="0 0 34 34" aria-hidden="true">
        <path d="M20 5H6a3 3 0 0 0-3 3v20a3 3 0 0 0 3 3h20a3 3 0 0 0 3-3V20" fill="none" stroke="#fff" stroke-width="3"/>
        <path d="M12 22c0-7 5-11 13-11V6l7 7-7 7v-5c-6 0-10 2-13 7z" fill="#fff"/>
      </svg>
    </div>
    <div class="stat__body"><div class="stat__value">1</div><span class="stat__label"></span></div>
  </section>

  <section class="abs stat" style="left:910px">
    <div class="stat__icon" style="background:var(--slate)">
      <svg width="38" height="34" viewBox="0 0 38 34" aria-hidden="true">
        <path d="M19 31L5 17C0 12 2 4 9 3c4-1 7 1 10 5 3-4 6-6 10-5 7 1 9 9 4 14z" fill="none" stroke="#fff" stroke-width="3" stroke-linejoin="round"/>
      </svg>
    </div>
    <div class="stat__body"><div class="stat__value">6</div><span class="stat__label"></span></div>
  </section>

  <section class="abs chart-panel">
    <svg width="1158" height="391" viewBox="9 148 526 178" aria-label="Views bar chart">
      <rect x="19" y="155" width="18" height="6" rx="1" fill="var(--green)"/>
      <rect x="503" y="156" width="24" height="5" rx="2.5" fill="var(--teal)"/>
      <text x="273" y="179" text-anchor="middle" font-family="Open Sans, sans-serif" font-weight="700" font-size="6.2" fill="#333">Views</text>
      <rect x="233" y="184" width="76" height="3.5" rx="1" fill="var(--ph)"/>
      <g stroke="var(--line)" stroke-width=".6">
        <line x1="44" y1="202" x2="520" y2="202"/><line x1="44" y1="226" x2="520" y2="226"/>
        <line x1="44" y1="250" x2="520" y2="250"/><line x1="44" y1="274" x2="520" y2="274"/>
      </g>
      <line x1="44" y1="298" x2="520" y2="298" stroke="#ccc" stroke-width=".8"/>
      <g fill="var(--ph)">
        <rect x="33" y="201" width="7" height="2"/><rect x="33" y="225" width="7" height="2"/>
        <rect x="33" y="249" width="7" height="2"/><rect x="33" y="273" width="7" height="2"/>
        <rect x="33" y="297" width="7" height="2"/>
        <rect x="23" y="230" width="3" height="38"/>
        <rect x="74" y="301" width="20" height="2.5"/><rect x="153" y="301" width="20" height="2.5"/>
        <rect x="236" y="301" width="12" height="2.5"/><rect x="317" y="301" width="9" height="2.5"/>
        <rect x="396" y="301" width="8" height="2.5"/><rect x="469" y="297" width="20" height="2"/>
        <rect x="236" y="313" width="10" height="3"/><rect x="260" y="313" width="55" height="3"/>
      </g>
      <g fill="var(--teal)">
        <rect x="58" y="217" width="19" height="81"/><rect x="137" y="270" width="20" height="28"/>
        <rect x="216" y="276" width="20" height="22"/><rect x="296" y="294" width="19" height="4"/>
        <rect x="375" y="294" width="19" height="4"/>
        <circle cx="231.5" cy="314.5" r="2"/>
      </g>
      <g fill="var(--orange)">
        <rect x="89" y="278" width="20" height="20"/><rect x="248" y="291" width="20" height="7"/>
        <rect x="327" y="295" width="20" height="3"/><rect x="407" y="295" width="19" height="3"/>
        <circle cx="255.5" cy="314.5" r="2"/>
      </g>
    </svg>
  </section>

</div>
</body>
</html>
```